business card for mobile ultrasound business
Coastline Portable Scans
business card for mobile ultrasound business - Medical
Creative Brief
Professional
Theodore R. Dalby
Senior Executive
738 Heron Bluff Lane Myrtle Beach, SC 29461
coastlineportablescans@mailbox-example.net

```html
<!DOCTYPE html>
<html lang="en">
<head>
<meta charset="utf-8">
<title>Coastline Portable Scans – Business Card</title>
<link href="https://fonts.googleapis.com/css2?family=Montserrat:wght@400;500;700&display=swap" rel="stylesheet">
<style>
  :root{
    --backdrop:#d9dadc;
    --paper:#ffffff;
    --ink:#2b2f36;
    --ink-soft:#5a6069;
    --navy:#0b3e66;
    --blue:#1677b3;
    --sky:#4fb3e6;
    --night:#050608;
  }
  *{margin:0;padding:0;box-sizing:border-box}
  html,body{width:1200px;height:895px;overflow:hidden}
  body{background:var(--backdrop);font-family:"Montserrat",Arial,sans-serif;position:relative}

  .card{position:absolute;width:620px;height:354px;overflow:hidden;box-shadow:0 6px 18px rgba(0,0,0,.18)}
  .card svg.card-art{position:absolute;inset:0;width:100%;height:100%}

  .card-back{left:520px;top:70px;background:var(--night)}
  .card-front{left:60px;top:470px;background:var(--paper)}

  .brand{position:absolute;display:flex;align-items:center;gap:8px;font-weight:700;letter-spacing:.5px}
  .brand-dot{width:14px;height:14px;border-radius:50%;background:var(--sky);flex:none}
  .card-back .brand{left:0;right:0;top:160px;justify-content:center;color:var(--sky);font-size:22px}
  .card-front .brand{left:28px;top:34px;color:var(--blue);font-size:17px}

  .person{position:absolute;right:30px;top:100px;text-align:right}
  .person-name{font-size:19px;font-weight:500;letter-spacing:2px;color:var(--ink)}
  .person-title{font-size:9px;font-weight:500;letter-spacing:1.5px;color:var(--ink-soft);margin-top:6px}

  .contact{position:absolute;top:222px;font-size:10px;line-height:17px;color:var(--ink-soft);white-space:nowrap}
  .contact-web{left:28px;width:250px}
  .contact-address{left:296px}
  .contact-phone{right:30px;text-align:right}
</style>
</head>
<body>

<section class="card card-back" aria-label="Card back">
  <svg class="card-art" viewBox="0 0 620 354" aria-hidden="true">
    <defs>
      <linearGradient id="barBlue" x1="0" y1="0" x2="1" y2="0">
        <stop offset="0" stop-color="#0b3e66"/>
        <stop offset=".5" stop-color="#4fb3e6"/>
        <stop offset="1" stop-color="#0b3e66"/>
      </linearGradient>
    </defs>
    <rect width="620" height="354" fill="url(#barBlue)"/>
    <polygon fill="#050608" points="0,72 60,72 80,56 540,56 560,72 620,72 620,282 560,282 540,298 80,298 60,282 0,282"/>
    <polyline points="50,20 62,32 50,44" fill="none" stroke="#e8f4fb" stroke-width="2"/>
    <polyline points="570,310 558,322 570,334" fill="none" stroke="#e8f4fb" stroke-width="2"/>
  </svg>
  <div class="brand"><span class="brand-dot"></span>Coastline Portable Scans</div>
</section>

<section class="card card-front" aria-label="Card front">
  <svg class="card-art" viewBox="0 0 620 354" aria-hidden="true">
    <defs>
      <linearGradient id="bandBlue" x1="0" y1="0" x2="1" y2="0">
        <stop offset="0" stop-color="#0b3e66"/>
        <stop offset=".5" stop-color="#1677b3"/>
        <stop offset="1" stop-color="#0b3e66"/>
      </linearGradient>
      <linearGradient id="footBlue" x1="0" y1="0" x2="1" y2="0">
        <stop offset="0" stop-color="#0b3e66"/>
        <stop offset=".5" stop-color="#4fb3e6"/>
        <stop offset="1" stop-color="#0b3e66"/>
      </linearGradient>
    </defs>
    <rect class="info-band" x="0" y="150" width="620" height="50" fill="url(#bandBlue)"/>
    <polygon points="160,150 172,150 192,175 172,200 160,200 180,175" fill="#ffffff"/>
    <polygon points="390,150 402,150 422,175 402,200 390,200 410,175" fill="#ffffff"/>
    <g fill="none" stroke="#ffffff" stroke-width="1.6">
      <circle cx="70" cy="175" r="10"/>
      <ellipse cx="70" cy="175" rx="4.5" ry="10"/>
      <line x1="60" y1="175" x2="80" y2="175"/>
    </g>
    <path d="M290 163a8 8 0 0 1 8 8c0 6-8 15-8 15s-8-9-8-15a8 8 0 0 1 8-8z" fill="#ffffff"/>
    <circle cx="290" cy="171" r="3" fill="#1677b3"/>
    <rect x="512" y="162" width="14" height="25" rx="2.5" fill="none" stroke="#ffffff" stroke-width="1.8"/>
    <line x1="517" y1="183" x2="521" y2="183" stroke="#ffffff" stroke-width="1.8"/>
    <polygon points="0,318 280,318 300,306 320,318 620,318 620,354 0,354" fill="url(#footBlue)"/>
  </svg>

  <div class="brand"><span class="brand-dot"></span>Coastline Portable Scans</div>

  <div class="person">
    <p class="person-name">THEODORE R. DALBY</p>
    <p class="person-title">SENIOR EXECUTIVE</p>
  </div>

  <div class="contact contact-web">
    <p>coastlineportablescans@mailbox-example.net</p>
    <p>www.coastline-scans-example.net</p>
  </div>
  <div class="contact contact-address">
    <p>738 Heron Bluff Lane</p>
    <p>Myrtle Beach, SC 29461</p>
  </div>
  <div class="contact contact-phone">
    <p>843 555 0142</p>
    <p>843 555 0142</p>
  </div>
</section>

</body>
</html>
```